Redesign for existing homepage

We would like a redesign for our websites 2 column homepage
We provide engine repair and reconditioning services
We would like a cleaner, modern site that works well with our logo colors
Please see the attached brief for more info
Target Market(s)
25 - 45
Industry/Entity Type
Cleaner
Requirements
Must have
- Google Fonts

```html
<!DOCTYPE html>
<html lang="en">
<head>
<meta charset="utf-8">
<title>Harlow Engines – Engine Repairs and Reconditioning</title>
<link href="https://fonts.googleapis.com/css2?family=Questrial&display=swap" rel="stylesheet">
<style>
:root{
  --ink:#1e1e1e;
  --blue:#1c4fe6;
  --yellow:#ffe600;
  --gold:#f7bf2e;
  --gold-dark:#eeab14;
  --nav:#fbc646;
  --text:#5a5a5a;
  --panel:#f6f6f6;
  --line:#e2e2e2;
  --footer:#3b3b3b;
}
*{margin:0;padding:0;box-sizing:border-box}
html,body{width:960px;height:1200px;overflow:hidden;background:#fff}
body{font-family:"Questrial",sans-serif;color:var(--text);position:relative}
.abs{position:absolute}
.site-header{position:absolute;left:0;top:0;width:960px;height:127px;background:radial-gradient(ellipse at 30% 20%,#3a3a3a,var(--ink) 60%)}
.brand{left:104px;top:40px;display:flex;align-items:center;gap:10px}
.brand-mark{width:44px;height:44px;border-radius:50%;background:var(--blue)}
.brand-name{color:var(--yellow);font-size:22px}
.tagline{left:330px;top:22px;width:300px;text-align:center}
.tagline h1{font-weight:400;color:var(--yellow);font-size:23px;line-height:26px}
.tagline p{color:#fff;font-size:17px;margin-top:5px}
.call-box{left:647px;top:34px;width:209px;height:60px;background:var(--blue);text-align:center;color:#fff;font-size:12.5px;line-height:15px;padding-top:4px}
.call-box strong{display:block;font-weight:400;color:var(--yellow);font-size:17px;margin-top:3px}
.main-nav{position:absolute;left:0;top:127px;width:960px;height:46px;background:linear-gradient(#fcd064,var(--nav))}
.main-nav ul{list-style:none;display:flex;justify-content:space-between;width:758px;margin-left:101px;line-height:46px;font-size:11.8px;color:#222}
.hero{left:104px;top:176px;width:752px;height:298px;background:#dcdcdc}
.hero-inner{position:absolute;left:4px;top:4px;width:744px;height:290px;background:#0c0c0c;overflow:hidden}
.hero-photo{position:absolute;right:0;top:0;width:470px;height:290px;background:linear-gradient(90deg,#0c0c0c 0%,#2b2f36 35%,#6a7382 65%,#b9c0c9 100%)}
.hero-copy{position:absolute;left:31px;top:30px;width:420px}
.hero-copy h2{font-weight:400;color:var(--yellow);font-size:22.5px}
.hero-copy h3{font-weight:400;color:#fff;font-size:19px;margin-top:4px}
.checklist{list-style:none;margin-top:14px;font-size:11.6px;color:#f2d84a;line-height:18px}
.checklist li{position:relative;padding-left:22px;margin-bottom:6.5px}
.checklist svg{position:absolute;left:0;top:4px}
.btn-blue{display:inline-block;background:var(--blue);color:#fff;font-size:15px;padding:0 20px;line-height:38px;margin-top:10px}
.dots{position:absolute;left:432px;top:268px;display:flex;gap:7px}
.dots i{width:7px;height:7px;border-radius:50%;background:#fff}
.dots i:first-child{background:var(--yellow)}
.welcome{left:104px;top:496px;width:496px}
.welcome h2{font-weight:400;color:var(--blue);font-size:19.5px}
.welcome p{font-size:10.4px;line-height:18.4px;margin-top:8px}
.read-more{display:block;color:var(--blue);font-size:10.5px;margin-top:13px}
.card{background:var(--panel);border:1px solid var(--line);width:240px}
.card h3{font-weight:400;color:var(--blue);font-size:16.5px;line-height:21px}
.feature{top:676px;height:324px;padding:11px 14px}
.feature .photo{width:211px;height:104px;margin-top:8px}
.feature p{font-size:10.4px;line-height:18.4px;margin-top:11px}
.btn-gold{display:inline-block;background:linear-gradient(var(--gold),var(--gold-dark));color:#222;font-size:13.5px;line-height:34px;padding:0 18px}
.feature .btn-gold{margin-top:11px}
.badge{top:1017px;height:80px;display:flex;align-items:center;gap:10px;padding-left:13px}
.badge p{color:#333;font-size:12px;margin-top:4px}
.sidebar{left:616px;top:500px;width:240px;height:611px;background:var(--panel);border:1px solid var(--line)}
.promo{position:absolute;left:12px;width:215px;background:#fff;border:1px solid #ececec;text-align:center;padding:12px 8px 0;box-shadow:0 6px 6px -5px rgba(0,0,0,.25)}
.promo h3{font-weight:400;color:var(--blue);font-size:17px;line-height:21px}
.promo p{font-size:10.4px;line-height:18.4px;margin-top:8px}
.promo .btn-gold{width:150px;margin-top:13px;padding:0}
.site-footer{position:absolute;left:0;top:1128px;width:960px;height:72px;background:var(--footer);color:#bbb;font-size:9.5px}
.site-footer .legal{position:absolute;left:104px;top:21px;line-height:18px}
.site-footer .legal span{color:var(--gold)}
.social{position:absolute;left:769px;top:24px;display:flex;gap:5px}
.social i{width:26px;height:26px;border-radius:50%;background:#6a6a6a}
</style>
</head>
<body>
<header class="site-header">
  <div class="abs brand"><span class="brand-mark"></span><span class="brand-name">Harlow Engines</span></div>
  <div class="abs tagline"><h1>Engine repairs and reconditioning specialists</h1><p>Greater Wellington</p></div>
  <div class="abs call-box">Call us to get your engine<br>running perfectly<strong>Petone: (04) 555 0142</strong></div>
</header>
<nav class="main-nav"><ul><li>Home</li><li>About Us</li><li>Private Vehicle Service &amp; Repair</li><li>TradeCustomers</li><li>Race &amp; Classic Car Engines</li><li>Make an Enquiry</li><li>Contact Us</li></ul></nav>

<section class="abs hero">
  <div class="hero-inner">
    <div class="hero-photo" role="img" aria-label="Mechanic in blue overalls inspecting an open car engine bay"></div>
    <div class="hero-copy">
      <h2>Specialist Engine Repair &amp; Reconditioning</h2>
      <h3>To have your car running at its best</h3>
      <ul class="checklist">
        <li><svg width="12" height="10" viewBox="0 0 12 10"><path d="M1 5l3.5 3.5L11 1" fill="none" stroke="#1c6ff0" stroke-width="2.2"/></svg>Do you have a personal or family car that needs a repair?</li>
        <li><svg width="12" height="10" viewBox="0 0 12 10"><path d="M1 5l3.5 3.5L11 1" fill="none" stroke="#1c6ff0" stroke-width="2.2"/></svg>Have a classic car that needs specialist engine work?</li>
        <li><svg width="12" height="10" viewBox="0 0 12 10"><path d="M1 5l3.5 3.5L11 1" fill="none" stroke="#1c6ff0" stroke-width="2.2"/></svg>Own a race car that needs specialist engine repairs?</li>
        <li><svg width="12" height="10" viewBox="0 0 12 10"><path d="M1 5l3.5 3.5L11 1" fill="none" stroke="#1c6ff0" stroke-width="2.2"/></svg>Are you a garage owner, needing to outsource an engine machining job from one of your customers?</li>
      </ul>
      <span class="btn-blue">Make an Enquiry</span>
    </div>
    <div class="dots"><i></i><i></i><i></i><i></i></div>
  </div>
</section>

<section class="abs welcome">
  <h2>Welcome to Our Webstie</h2>
  <p>Aliquam molestie, mi et imperdiet euismod, dui purus auctor tellus, et interdum lacus lectus et ante. Sed accumsan sollicitudin sapien, sit amet adipiscing turpis gravida ac. In congue, neque ac lobortis volutpat, libero mauris varius mi, vitae suscipit ipsum ligula vitae risus. Duis aliquam nibh a dui iaculis viverra id a velit. Vivamus egestas risus in magna varius commodo. Sed semper viverra egestas. Etiam pretium porttitor lectus, vel ornare neque porta volutpat.</p>
  <span class="read-more">READ MORE ››</span>
</section>

<article class="abs card feature" style="left:104px">
  <h3>Interested in becoming<br>a trade customer?</h3>
  <div class="photo" role="img" aria-label="Man leaning over a smoking car engine" style="background:linear-gradient(135deg,#8a7a62,#d9d6cf 45%,#3a3a38)"></div>
  <p>Aliquam molestie, mi et imperdiet euismod, dui purus auctor tellus, et interdum lacus lectus et ante. Sed accumsan sollicitudin sapien, sit amet adipiscing turpis gravida ac.</p>
  <span class="btn-gold">Read More</span>
</article>
<article class="abs card feature" style="left:360px">
  <h3>Race &amp; Classic Car<br>Engine</h3>
  <div class="photo" role="img" aria-label="Chrome V8 race engine with blue ignition leads" style="background:linear-gradient(135deg,#1b2a4a,#7a808a 45%,#9a4a2a 80%,#2a3a6a)"></div>
  <p>Aliquam molestie, mi et imperdiet euismod, dui purus auctor tellus, et interdum lacus lectus et ante. Sed accumsan sollicitudin sapien, sit amet adipiscing turpis gravida ac.</p>
  <span class="btn-gold">Read More</span>
</article>

<div class="abs card badge" style="left:104px">
  <svg width="46" height="54"><rect width="46" height="54" fill="#ffe600" stroke="#c9b400"/></svg>
  <div><h3>Official stockists of</h3><p>Southline Cylinder Heads</p></div>
</div>
<div class="abs card badge" style="left:360px">
  <svg width="80" height="48"><ellipse cx="40" cy="24" rx="40" ry="24" fill="#111"/></svg>
  <div><h3>As a Member of</h3><p>Engine Rebuilders Guild</p></div>
</div>

<aside class="abs sidebar">
  <div class="promo" style="top:12px;height:174px">
    <h3>Need service and repair<br>for a private vehicle?</h3>
    <p>Get an efficient and honest diagnosis, along with repair work that will have your car running smoothly.</p>
    <span class="btn-gold">Make an Enquiry</span>
  </div>
  <div class="promo" style="top:204px;height:174px">
    <h3>Interested in becoming<br>a trade customer?</h3>
    <p>You can outsource your the specialist machining jobs to us at very competitive rates.</p>
    <span class="btn-gold">Trade Customers</span>
  </div>
  <div class="promo" style="top:395px;height:188px">
    <h3>Is your classic or race car<br>your passion?</h3>
    <p>Is your vintage car just sitting in your garage? Contact us to get the engine on your classic car or race car repaired or overhauled.</p>
    <span class="btn-gold" style="margin-top:8px">Trade Customers</span>
  </div>
</aside>

<footer class="site-footer">
  <div class="legal">Copyright © 2014. <span>Harlow Engines</span>. All Right Reserved<br>Term of Services</div>
  <div class="social"><i></i><i></i><i></i></div>
</footer>
</body>
</html>
```